Creating a Label for the Wine "Fold the Sails"

As the name suggest, this wine is the one people must to take home. Fold the sails is the perfect wine to drink at home with you family and friends. Customers should be able to associate this label with happy moments spent with their loved ones. The dimensions can be between 9cm x 11,5 and 12cm x 8 cm.

```html
<!DOCTYPE html>
<html lang="en">
<head>
<meta charset="utf-8">
<title>Fold the Sails – Wine Label</title>
<link rel="stylesheet" href="https://fonts.googleapis.com/css2?family=Dancing+Script:wght@500&family=Lora:ital,wght@1,700&display=swap">
<style>
  :root {
    --page: #ffffff;
    --label-light: #fbfbfa;
    --label-edge: #dcdcda;
    --frame: #3a302c;
    --frame-inner: #8d8580;
    --ink: #3b2a24;
    --damask: #ece8df;
    --road-light: #f4f5f7;
    --road-mid: #c9ccd3;
    --corner: #8a7d70;
  }
  * { box-sizing: border-box; margin: 0; padding: 0; }
  html, body {
    width: 901px; height: 1200px; overflow: hidden;
    background: var(--page);
  }
  .canvas {
    position: relative; width: 901px; height: 1200px;
  }
  .wine-label {
    position: absolute; left: 70px; top: 112px;
    width: 760px; height: 976px;
    border: 3px solid var(--frame);
    background: radial-gradient(ellipse at 50% 42%, var(--label-light) 0%, #f1f1f0 60%, var(--label-edge) 100%);
  }
  .wine-label__inner-frame {
    position: absolute; inset: 12px;
    border: 1px solid var(--frame-inner);
  }
  .corner-ornament {
    position: absolute; width: 34px; height: 34px;
    background: var(--corner); opacity: 0.55; border-radius: 4px;
  }
  .corner-ornament--tl { left: 20px; top: 20px; }
  .corner-ornament--tr { right: 20px; top: 20px; }
  .corner-ornament--bl { left: 20px; bottom: 20px; }
  .corner-ornament--br { right: 20px; bottom: 20px; }
  .damask-motif {
    position: absolute; left: 225px; top: 130px;
    width: 310px; height: 500px;
    background: radial-gradient(ellipse at 50% 50%, var(--damask) 0%, rgba(236,232,223,0.5) 55%, rgba(236,232,223,0) 75%);
  }
  .road-scene {
    position: absolute; left: 15px; right: 15px; bottom: 15px; height: 200px;
    background: linear-gradient(180deg, rgba(244,245,247,0) 0%, var(--road-light) 35%, var(--road-mid) 70%, var(--road-light) 100%);
  }
  .wine-name {
    position: absolute; left: 0; right: 0; top: 360px;
    text-align: center;
    font-family: "Dancing Script", cursive;
    font-weight: 500;
    font-size: 124px; line-height: 1;
    color: var(--ink);
  }
  .wine-details {
    position: absolute; right: 20px; top: 780px;
    transform-origin: right top;
    transform: rotate(-90deg) translateY(-100%);
    white-space: nowrap;
    font-family: "Lora", serif;
    font-style: italic; font-weight: 700;
    font-size: 17px; color: var(--ink);
    letter-spacing: 0.5px;
  }
</style>
</head>
<body>
  <main class="canvas">
    <section class="wine-label">
      <div class="wine-label__inner-frame"></div>
      <div class="corner-ornament corner-ornament--tl" role="img" aria-label="Small floral corner ornament"></div>
      <div class="corner-ornament corner-ornament--tr" role="img" aria-label="Small floral corner ornament"></div>
      <div class="corner-ornament corner-ornament--bl" role="img" aria-label="Small floral corner ornament"></div>
      <div class="corner-ornament corner-ornament--br" role="img" aria-label="Small floral corner ornament"></div>
      <div class="damask-motif" role="img" aria-label="Faint damask ornament behind the wine name"></div>
      <div class="road-scene" role="img" aria-label="Soft misty photo of a winding road leading home"></div>
      <h1 class="wine-name">Fold the Sails</h1>
      <p class="wine-details">Red wine 0,75l, 13%alc</p>
    </section>
  </main>
</body>
</html>
```